Brookvale Renovations - Get the creative juices going!!

Brookvale does not do the actual renovation work. The company provides high end project management of renovation (primarily residential - with an eye toward commercial) The renovation work could look very different between projects. This company manages the work of contractors, architects and interior designers (either subcontracted directly by Brookvale or hired by the client and entrusted to Brookvale to manage). Clients are high end in the economic scale and the card needs to have a high end feel to it.

The owner is female, but the audience will be heavily slanted male. It should not be a "feminine" or "masculine" looking card. If anything, slant more on the masculine side. Clean, simple, yet creative and artistically appealing. The card design should complement and in no way compete with the logo.

When people think of our company: trust, integrity, dynamic, limitless possibilities, transition, energy, creative. We plan to expand in the future to be international.

There will also be a contest running for stationary. Please check that section, as well.

***Black is 80-90 percent black. Not stark black

Tight timeline. Needs cards printed quickly!

```html
<!DOCTYPE html>
<html lang="en">
<head>
<meta charset="UTF-8">
<title>Brookvale Renovations – Business Card</title>
<link rel="stylesheet" href="https://fonts.googleapis.com/css2?family=Open+Sans:wght@400;600;700&display=swap">
<style>
  :root {
    --backdrop: #d9d6d1;
    --card: #262626;
    --ink: #f2f2f2;
    --muted: #cfcfcf;
    --accent: #1fa39a;
    --rule: #4a4a4a;
  }
  * { box-sizing: border-box; margin: 0; padding: 0; }
  html, body {
    width: 1200px; height: 900px; overflow: hidden;
    background: var(--backdrop);
    font-family: "Open Sans", Arial, sans-serif;
  }
  .sheet {
    width: 1200px; height: 900px;
    display: flex; flex-direction: column;
    align-items: center; justify-content: center; gap: 50px;
  }
  .card {
    width: 620px; height: 354px;
    background: var(--card);
    border-radius: 4px;
    box-shadow: 0 4px 14px rgba(0,0,0,0.18);
    position: relative;
    color: var(--ink);
  }
  .card--front {
    display: flex; align-items: center; justify-content: center;
  }
  .brand {
    display: flex; align-items: center; gap: 14px;
    font-weight: 600; text-transform: uppercase;
    color: var(--ink); white-space: nowrap;
  }
  .brand__square {
    width: 22px; height: 22px; border: 2px solid var(--ink);
  }
  .card--front .brand { font-size: 30px; letter-spacing: 3px; }
  .card--back .brand {
    position: absolute; top: 66px; left: 168px;
    font-size: 24px; letter-spacing: 2px;
  }
  .card--back .brand__square { width: 18px; height: 18px; }
  .details {
    position: absolute; top: 156px; left: 0; right: 0;
    display: flex; align-items: stretch;
  }
  .details__person {
    width: 236px; text-align: right; padding-right: 18px;
  }
  .person__name {
    color: var(--accent); font-weight: 600; font-size: 14px;
    letter-spacing: 0.5px; margin-bottom: 6px;
  }
  .person__address { font-size: 13px; line-height: 1.45; color: var(--muted); }
  .details__divider { width: 1px; background: var(--rule); }
  .details__contact {
    list-style: none; padding-left: 16px;
    display: flex; flex-direction: column; gap: 7px;
    font-size: 17px; letter-spacing: 0.3px;
  }
  .contact__item { display: flex; align-items: center; gap: 9px; }
  .contact__icon { width: 15px; height: 15px; flex: none; }
</style>
</head>
<body>
<main class="sheet">
  <section class="card card--front" aria-label="Card front">
    <div class="brand"><span class="brand__square"></span>Brookvale Renovations</div>
  </section>

  <section class="card card--back" aria-label="Card back">
    <div class="brand"><span class="brand__square"></span>Brookvale Renovations</div>
    <div class="details">
      <div class="details__person">
        <p class="person__name">DANA HOLLIS - Owner</p>
        <p class="person__address">118 Millbrook Road, Box 42,<br>Ashford, New York 10590</p>
      </div>
      <div class="details__divider"></div>
      <ul class="details__contact">
        <li class="contact__item">
          <svg class="contact__icon" viewBox="0 0 16 16"><rect width="16" height="16" rx="2" fill="#1fa39a"/><path d="M5 3.5c.6 0 1 .9 1.2 1.6.1.5-.5.8-.7 1.1.5 1.3 1.4 2.3 2.6 2.9.3-.3.6-.9 1.1-.8.7.2 1.7.6 1.6 1.2-.1.9-.9 1.5-1.8 1.4C6 10.6 3.6 8 3.5 5.2c0-.9.7-1.7 1.5-1.7z" fill="#262626"/></svg>
          914.555.0147
        </li>
        <li class="contact__item">
          <svg class="contact__icon" viewBox="0 0 16 16"><rect width="16" height="16" rx="2" fill="#1fa39a"/><rect x="3" y="4.5" width="10" height="7" fill="none" stroke="#262626" stroke-width="1.3"/><path d="M3 4.5l5 4 5-4" fill="none" stroke="#262626" stroke-width="1.3"/></svg>
          brookvale.renovations@mailbox.com
        </li>
        <li class="contact__item">
          <svg class="contact__icon" viewBox="0 0 16 16"><circle cx="8" cy="8" r="7.5" fill="#1fa39a"/><g fill="none" stroke="#262626" stroke-width="1"><circle cx="8" cy="8" r="5"/><ellipse cx="8" cy="8" rx="2.2" ry="5"/><path d="M3 8h10M4 5.5h8M4 10.5h8"/></g></svg>
          www.brookvale-renovations.com
        </li>
      </ul>
    </div>
  </section>
</main>
</body>
</html>
```